Electrician Letterhead Design RMV

We need some letterhead for our bills and other papers.
Customer address is on the right side (Swiss format)
A4 format

Design should also be applicable on Cards

Target Market(s)

Private Customers, Small Business

Industry/Entity Type

Electrician

Other font styles liked:
• incised 901

Colors
00AB8E
00BBA5
67D7C9
C6EFE9
E9F9F6

```html
<!DOCTYPE html>
<html lang="en">
<head>
<meta charset="utf-8">
<title>RMV Letterhead</title>
<link href="https://fonts.googleapis.com/css2?family=Play:wght@400;700&family=Noto+Sans:wght@400;500&family=Great+Vibes&display=swap" rel="stylesheet">
<style>
:root{
  --teal:#00ab8e;
  --teal-2:#00bba5;
  --mint:#67d7c9;
  --backdrop:#c6efe9;
  --paper:#e9f9f6;
  --ink:#3a3f3e;
  --white:#ffffff;
}
*{margin:0;padding:0;box-sizing:border-box}
html,body{width:1200px;height:1000px;overflow:hidden;background:var(--backdrop)}
.canvas{position:relative;width:1200px;height:1000px;background:var(--backdrop)}
.letterhead{position:absolute;left:340px;top:140px;width:482px;height:675px;background:var(--paper);overflow:hidden;font-family:"Noto Sans",Verdana,sans-serif;color:var(--ink)}
.abs{position:absolute}
.brand-band{left:0;top:40px;width:246px;height:61px;background:var(--teal)}
.brand-name{left:48px;top:8px;font-family:"Play",sans-serif;font-weight:700;font-size:38px;color:var(--white);letter-spacing:1px;line-height:44px}
.edge-bar{left:460px;width:22px;background:var(--teal)}
.edge-top{top:40px;height:123px}
.edge-bottom{top:515px;height:120px}
.card{border:2px solid var(--teal);border-radius:9px;background:var(--paper)}
.card-title{position:absolute;left:0;right:0;text-align:center;font-family:"Play",sans-serif;font-size:11.5px;color:var(--teal)}
.card-bar{position:absolute;left:0;right:0;height:13px;background:var(--teal);color:var(--white);font-size:9px;line-height:13px}
.card-row{position:absolute;font-size:9px;line-height:12px;display:flex;align-items:center;gap:8px;color:var(--ink)}
.card-row svg{width:9px;height:9px;fill:var(--teal);flex:none}
.address-card{left:265px;top:38px;width:179px;height:127px}
.address-card .card-title{top:1px}
.address-card .card-bar{top:16px;padding-left:14px}
.address-card .card-bar svg{width:8px;height:8px;fill:var(--white);vertical-align:-1px;margin-right:9px}
.address-card .card-row{left:13px}
.care-card{left:267px;top:515px;width:178px;height:122px}
.care-card .card-title{top:1px}
.care-card .card-bar{top:16px;text-align:center}
.care-card .card-bar svg{position:absolute;right:8px;top:3px;width:8px;height:8px;fill:var(--white)}
.care-card .card-row{right:10px;justify-content:flex-end}
.heading{font-family:"Play",sans-serif;font-size:14px;color:var(--teal);line-height:16px}
.label{font-size:9.5px;letter-spacing:1px;line-height:12px}
.small{font-size:9.5px;line-height:11.5px}
.date-line{font-size:9.5px;letter-spacing:1.8px;text-align:right}
.body-copy{left:39px;top:286px;width:404px;font-size:9.3px;line-height:11.3px;text-align:justify}
.body-copy p{margin-bottom:11.3px}
.signature{font-family:"Great Vibes",cursive;font-size:18px;color:var(--teal);line-height:20px}
.corner-shape{left:0;top:600px}
</style>
</head>
<body>
<div class="canvas">
  <div class="letterhead">
    <div class="abs brand-band"><div class="abs brand-name">RMV</div></div>
    <div class="abs edge-bar edge-top"></div>
    <div class="abs edge-bar edge-bottom"></div>

    <div class="abs card address-card">
      <div class="card-title">Customer Address</div>
      <div class="card-bar"><svg viewBox="0 0 10 10"><circle cx="5" cy="5" r="4" fill="none" stroke="#fff" stroke-width="1.6"/><circle cx="5" cy="5" r="1.6"/></svg>Customer ID Number</div>
      <div class="card-row" style="top:33px"><svg viewBox="0 0 10 10"><circle cx="5" cy="3" r="2.4"/><path d="M0.5 10c0-3 2-4.5 4.5-4.5S9.5 7 9.5 10z"/></svg>Customer Name</div>
      <div class="card-row" style="top:51px"><svg viewBox="0 0 10 10"><path d="M2 0.5l2 2.2-1 1.4c.6 1.3 1.6 2.3 2.9 2.9l1.4-1 2.2 2-1.2 1.7C4.6 9.6.4 5.4.3 1.7z"/></svg>+000 123 4567</div>
      <div class="card-row" style="top:69px"><svg viewBox="0 0 10 10"><path d="M0 4.5L10 0 7 10 5 6z"/></svg>customer@mail.com</div>
      <div class="card-row" style="top:87px"><svg viewBox="0 0 10 10"><path d="M5 0a3.6 3.6 0 0 1 3.6 3.6C8.6 6.2 5 10 5 10S1.4 6.2 1.4 3.6A3.6 3.6 0 0 1 5 0zm0 2a1.5 1.5 0 1 0 0 3 1.5 1.5 0 0 0 0-3z"/></svg>123, Street, City, Country, 000.</div>
      <div class="card-row" style="top:105px"><svg viewBox="0 0 10 10"><circle cx="5" cy="5" r="4.5"/><path d="M1 5h8M5 .5v9" stroke="#e9f9f6" stroke-width="1"/></svg>www.website.com</div>
    </div>

    <div class="abs" style="left:39px;top:128px">
      <div class="heading">To</div>
      <div class="heading">YOUR NAME</div>
      <div class="label">Position Name</div>
    </div>

    <div class="abs" style="left:39px;top:190px">
      <div class="heading" style="font-size:14.5px">ELEKTROTECHNIK ROVAN Gmbh</div>
      <div class="small">Tel : +000 123 4567</div>
      <div class="small">Mail : mail@company.com</div>
      <div class="small">Website : www.company.com</div>
    </div>

    <div class="abs" style="right:38px;top:218px;text-align:right">
      <div class="heading">DATE</div>
      <div class="date-line">SUN DD/MM/YYYY 00:00</div>
    </div>

    <div class="abs body-copy">
      <p>Lorem Ipsum is simply dummy text of the printing and typesetting industry. Lorem Ipsum has been the industry's standard dummy text ever since the 1500s, when an unknown printer took a galley of type and scrambled it to make a type specimen book. It has survived not only five centuries,</p>
      <p>but also the leap into electronic typesetting, remaining essentially unchanged. It was popularised in the 1960s with the release of Letraset sheets containing Lorem Ipsum passages, and more recently with desktop publishing software like Aldus PageMaker including versions of Lorem Ipsum.</p>
      <p>Lorem Ipsum is simply dummy text of the printing and typesetting industry. Lorem Ipsum has been the industry's standard dummy text ever since the 1500s, when an unknown printer took a galley of type and scrambled it to make a type specimen book. It has survived not only five centuries,</p>
      <p>Lorem Ipsum is simply dummy text of the printing and typesetting industry. Lorem Ipsum has been the industry's standard dummy text ever since the 1500s, when an unknown printer took a galley of type and scrambled it to make a type specimen book. It has survived not only five centuries,</p>
    </div>

    <div class="abs" style="left:39px;top:556px">
      <div class="signature">Your Name</div>
      <div class="heading">YOUR NAME</div>
      <div class="label">Position Name</div>
    </div>

    <div class="abs card care-card">
      <div class="card-title">Customer Care</div>
      <div class="card-bar">Hotline : 40250<svg viewBox="0 0 10 10"><circle cx="5" cy="5" r="4" fill="none" stroke="#fff" stroke-width="1.6"/><circle cx="5" cy="5" r="1.6"/></svg></div>
      <div class="card-row" style="top:40px">+000 123 4567<svg viewBox="0 0 10 10"><path d="M2 0.5l2 2.2-1 1.4c.6 1.3 1.6 2.3 2.9 2.9l1.4-1 2.2 2-1.2 1.7C4.6 9.6.4 5.4.3 1.7z"/></svg></div>
      <div class="card-row" style="top:58px">support@company.com<svg viewBox="0 0 10 10"><path d="M0 4.5L10 0 7 10 5 6z"/></svg></div>
      <div class="card-row" style="top:76px">123, Street, City, Country, 000.<svg viewBox="0 0 10 10"><path d="M5 0a3.6 3.6 0 0 1 3.6 3.6C8.6 6.2 5 10 5 10S1.4 6.2 1.4 3.6A3.6 3.6 0 0 1 5 0zm0 2a1.5 1.5 0 1 0 0 3 1.5 1.5 0 0 0 0-3z"/></svg></div>
      <div class="card-row" style="top:94px">www.company.com<svg viewBox="0 0 10 10"><circle cx="5" cy="5" r="4.5"/><path d="M1 5h8M5 .5v9" stroke="#e9f9f6" stroke-width="1"/></svg></div>
    </div>

    <svg class="abs corner-shape" width="90" height="75" viewBox="0 0 90 75"><polygon points="0,5 82,57 47,75 0,75" fill="var(--teal)"/></svg>
  </div>
</div>
</body>
</html>
```